Carwash Signage

We own and operate a 25m tunnel car wash in the uk. We are looking to upgrade our signage to include the following:-

Wash selection Board Size-1300x1300mm
Conditions 1300x1300mm
Instructions 1300x1300mm
Banner 2600x600mm
Stamp card flyer a5 double sided - 9 squares for stamping 3rd square needs to say free air freshener 9th square needs to say free vip car wash.

I have attached some notes for the details that are required to be included.

We are looking for a modern smart look more European car wash style than American car wash style. It should be bold and clear. with yellow/orange & blue/green,grey colours

The final design must be in a industry standard printable format.

UPDATED BRIEF AS DISCUSSED: We require design for 2 x window decals, flag design and 50% off voucher. Attached are rough layout drawings of what they should look like - we expect the designs to be in keeping with the previous designs colours, etc that have been carried out. We Look forward to hearing from you.

Target Market(s)

local car owners within a 15-20 mile radius

Colors
0054AA
0677BA
7BADD7
CADEEF
E8F1F8
0094D4
00A9DD
6FCCEA
C7EBF8
E9F6FB
00AB8E
00BBA5
67D7C9
C6EFE9
E9F9F6

Requirements
Must have
• must be sharp and modern European look

```html
<!DOCTYPE html>
<html lang="en">
<head>
<meta charset="utf-8">
<title>Harbourside Car Wash – Banner</title>
<link href="https://fonts.googleapis.com/css2?family=Poppins:wght@400;600;700;800;900&family=Open+Sans:wght@400&display=swap" rel="stylesheet">
<style>
  :root{
    --canvas:#fdfdfd;
    --panel:#e8e8f2;
    --navy:#2e3f98;
    --royal:#2d4aa2;
    --sky:#1f86cf;
    --ring:#2a8fd6;
    --white:#ffffff;
    --ink:#2a2f5a;
  }
  *{margin:0;padding:0;box-sizing:border-box}
  html,body{width:1200px;height:1200px;overflow:hidden;background:var(--canvas)}
  body{position:relative;font-family:"Poppins",sans-serif}

  .banner{position:absolute;left:22px;top:450px;width:1159px;height:268px;background:var(--panel)}
  .features{position:absolute;inset:0}
  .badge{position:absolute;width:72px;height:72px;border-radius:50%;display:flex;align-items:center;justify-content:center;text-align:center;font-weight:800;line-height:1.1;font-size:14px;text-transform:uppercase}
  .badge--solid{background:var(--navy);border:3px solid var(--ring);color:var(--white)}
  .badge--outline{background:var(--white);border:3px solid var(--navy);color:var(--navy)}
  .badge--large{font-size:16.5px}
  .badge--small{font-size:11px;line-height:1.2}

  .center-strip{position:absolute;left:387px;top:0;width:388px;height:8px;background:linear-gradient(90deg,var(--sky),var(--royal))}
  .brand{position:absolute;left:387px;top:24px;width:388px;text-align:center;color:var(--ink)}
  .brand__tag{display:block;font-size:11px;font-weight:400;letter-spacing:.3px;margin-left:96px;line-height:1.2}
  .brand__name{display:block;font-size:24px;font-weight:700;letter-spacing:1px;line-height:1.05}

  .headline-panel{position:absolute;left:387px;top:84px;width:388px;height:116px;background:linear-gradient(90deg,var(--sky),var(--royal))}
  .headline{position:absolute;left:0;right:0;top:6px;text-align:center;color:var(--white);font-weight:900;font-size:64px;letter-spacing:-1px;line-height:1.2}
  .hours{position:absolute;left:21px;top:87px;width:344px;height:22px;border-radius:11px;background:rgba(255,255,255,.14);display:flex;align-items:center;color:var(--white);font-family:"Open Sans",sans-serif;font-size:14px}
  .hours span{flex:1;text-align:center}
  .hours i{width:1px;height:13px;background:rgba(255,255,255,.7)}

  .illustration{position:absolute;left:790px;top:6px;width:350px;height:192px;border-radius:4px;background:radial-gradient(ellipse at 55% 55%,#f3c13a 0 22%,#b8d4ee 45%,var(--panel) 75%)}

  .notice-band{position:absolute;left:0;top:200px;width:1159px;height:68px;background:linear-gradient(90deg,var(--sky),var(--royal))}
  .notice{position:absolute;display:flex;align-items:center;color:var(--white);font-weight:700;line-height:1.2}
  .notice svg{width:36px;height:32px;flex:none;margin-right:13px}
  .notice--left{left:21px;top:18px;font-size:12px}
  .notice--right{left:801px;top:18px;font-size:12.5px}

  .payments{position:absolute;left:408px;top:14px;display:flex;gap:6px}
  .payments__label{width:129px;height:32px;border-radius:16px 0 0 16px;background:#2a7fc6;color:var(--white);font-family:"Open Sans",sans-serif;font-size:10.5px;display:flex;align-items:center;justify-content:center}
  .payments__cards{width:208px;height:32px;border-radius:0 16px 16px 0;background:#2a7fc6;display:flex;align-items:center;justify-content:space-around;padding:0 10px}
  .card{width:25px;height:15px;background:var(--white);border-radius:2px;color:var(--navy);font-weight:700;font-size:5.5px;display:flex;align-items:center;justify-content:center}
</style>
</head>
<body>
<section class="banner">
  <div class="features">
    <div class="badge badge--solid badge--large" style="left:23px;top:24px">Safe<br>Car</div>
    <div class="badge badge--outline" style="left:109px;top:24px">Happy<br>Engine</div>
    <div class="badge badge--solid" style="left:194px;top:24px">Clean<br>Look</div>
    <div class="badge badge--outline badge--large" style="left:280px;top:24px">No<br>Rust</div>
    <div class="badge badge--solid badge--small" style="left:60px;top:108px">Anti-<br>Bake<br>Brakes</div>
    <div class="badge badge--outline" style="left:146px;top:108px">Nice<br>Wheels</div>
    <div class="badge badge--solid" style="left:231px;top:108px">Deadly<br>Ash</div>
  </div>

  <div class="center-strip"></div>
  <div class="brand">
    <span class="brand__tag">CAR WASH</span>
    <span class="brand__name">HARBOURSIDE</span>
  </div>

  <div class="headline-panel">
    <h1 class="headline">CAR WASH</h1>
    <div class="hours"><span>MON-SAT / 08:00-18:00</span><i></i><span>SUN / 09:00-18:00</span></div>
  </div>

  <div class="illustration" role="img" aria-label="Illustration of three attendants washing a yellow car with foam and a pressure washer"></div>

  <div class="notice-band">
    <p class="notice notice--left">
      <svg viewBox="0 0 36 32" aria-hidden="true"><path d="M18 2 L34 30 H2 Z" fill="none" stroke="#fff" stroke-width="2.2" stroke-linejoin="round"/><rect x="16.6" y="11" width="2.8" height="11" rx="1.2" fill="#fff"/><circle cx="18" cy="25.5" r="1.6" fill="#fff"/></svg>
      We are not responsible for any potential damage!
    </p>

    <div class="payments">
      <div class="payments__label">Payments Accepted</div>
      <div class="payments__cards">
        <span class="card">Debit</span><span class="card">Online</span><span class="card">Credit</span><span class="card">Wallet</span><span class="card">Tap</span>
      </div>
    </div>

    <p class="notice notice--right">
      <svg viewBox="0 0 36 32" aria-hidden="true"><path d="M18 2 L34 30 H2 Z" fill="none" stroke="#fff" stroke-width="2.2" stroke-linejoin="round"/><rect x="16.6" y="11" width="2.8" height="11" rx="1.2" fill="#fff"/><circle cx="18" cy="25.5" r="1.6" fill="#fff"/></svg>
      <span>We are not responsible for damage to the car<br>or loss of belongings.</span>
    </p>
  </div>
</section>
</body>
</html>
```